Tarek & Lubna's 50th Anniversary Celebration & Reunion

I need a flyer to send out via email and for posting on chatterboard to invite guests to a 50th wedding anniversary / family reunion.

Location is sunny La Jolla CA the Pearl of San Diego's Shore.

Week long daily activities starting Mon July 28-Aug 1st Friday, The event will be on Wednesday.
* Daily Catered Family Breakfast at the Marlow Hall of La Jolla
* Daily group activities including
*Exploring La Jolla Beaches & Ocean Cave Kayaking
*TideRealm Private Behind the Scenes Tour
*World Famous Pellham Wildlife Park
*Sunset Balloon Ride
*Private Yatch on the Bay

Actual Anniversary event will take place Thursday December 28, 2013 at 5pm at the Marlow Hall.

There are many local hotels around the Marlow Hall. 4213 Brindle Ln, La Jolla, CA 92058

Host is Kamil and the entire Haddour Family. For questions, please email Kamil@thelinden-feasts.com

Target Market(s)

all ages from 10 year olds to 70 year olds. Should appeal to all

Industry/Entity Type

Wedding

Font styles to use
Script

Colors

Designer to choose colors to be used in the design.

Requirements
Must have
• Fun graphics, including one with a stretch limo as there will be one available

Photo enclosed
Nice to have
• Logo for TideRealm Inserting a picture of an actual wedding 50 years ago or so of the bride and groom. incorporating the limo cropped out of the picture attached would also be nice

```html
<!DOCTYPE html>
<html lang="en">
<head>
<meta charset="utf-8">
<title>Tarek &amp; Lubna's 50th Anniversary</title>
<link rel="stylesheet" href="https://fonts.googleapis.com/css2?family=Courgette&family=Oswald:wght@500&display=swap">
<style>
  :root {
    --page: #ece8e2;
    --card: #ffffff;
    --orange: #f2a530;
    --ink: #1c1c1c;
    --ribbon-text: #ffffff;
    --photo-light: #cfcfcf;
    --photo-dark: #4a4a4a;
  }
  * { box-sizing: border-box; margin: 0; padding: 0; }
  html, body { width: 1200px; height: 1200px; overflow: hidden; }
  body {
    background: var(--page);
    display: flex;
    align-items: center;
    justify-content: center;
    gap: 60px;
  }
  .card {
    position: relative;
    width: 480px;
    height: 840px;
    background: var(--card);
    overflow: hidden;
    box-shadow: 0 2px 8px rgba(0,0,0,0.15);
  }

  /* Front */
  .wedding-photo {
    position: absolute;
    inset: 0;
    background:
      radial-gradient(ellipse at 70% 35%, #eeeeee 0%, transparent 45%),
      linear-gradient(160deg, var(--photo-light) 0%, #9a9a9a 45%, var(--photo-dark) 100%);
  }
  .title-ribbons {
    position: absolute;
    left: 0;
    bottom: 70px;
    display: flex;
    flex-direction: column;
    align-items: flex-start;
    gap: 8px;
    font-family: "Oswald", sans-serif;
    font-weight: 500;
    color: var(--ribbon-text);
    text-transform: uppercase;
  }
  .ribbon {
    background: var(--orange);
    padding: 2px 40px 2px 34px;
    clip-path: polygon(0 0, 100% 0, calc(100% - 16px) 50%, 100% 100%, 0 100%, 16px 50%);
    line-height: 1.15;
  }
  .ribbon--name { font-size: 40px; letter-spacing: 1px; margin-left: 20px; }
  .ribbon--and { font-size: 22px; text-transform: none; margin-left: 80px; padding: 0 30px; }
  .ribbon--years { font-size: 24px; margin-left: 110px; padding: 0 30px; }
  .ribbon--years sup { font-size: 13px; }
  .ribbon--occasion { font-size: 22px; letter-spacing: 1px; margin-left: 30px; }

  /* Back */
  .stripes {
    position: absolute;
    top: 0;
    bottom: 0;
    width: 44px;
  }
  .stripes--right { right: 14px; }
  .stripes--left { left: 14px; }
  .stripe { position: absolute; top: 0; bottom: 0; background: var(--orange); }
  .stripe--wide { width: 18px; left: 0; }
  .stripe--thin { width: 10px; left: 28px; }
  .stripes--left .stripe--wide { left: 26px; }
  .stripes--left .stripe--thin { left: 6px; }

  .invitation {
    position: absolute;
    top: 46px;
    left: 70px;
    right: 70px;
    text-align: center;
    font-family: "Courgette", cursive;
    color: var(--ink);
    font-size: 19px;
    line-height: 1.35;
  }
  .invitation p { margin-bottom: 20px; }
  .invitation .couple { font-size: 21px; }
  .invitation .email { word-break: break-all; }
</style>
</head>
<body>

  <section class="card card--front">
    <div class="wedding-photo" role="img" aria-label="Black and white wedding photograph of the young bride and groom"></div>
    <div class="title-ribbons">
      <span class="ribbon ribbon--name">Tarek</span>
      <span class="ribbon ribbon--and">and</span>
      <span class="ribbon ribbon--name">Lubna's</span>
      <span class="ribbon ribbon--years">50<sup>th</sup></span>
      <span class="ribbon ribbon--occasion">Anniversary</span>
    </div>
  </section>

  <section class="card card--back">
    <div class="stripes stripes--left"><span class="stripe stripe--wide"></span><span class="stripe stripe--thin"></span></div>
    <div class="stripes stripes--right"><span class="stripe stripe--wide"></span><span class="stripe stripe--thin"></span></div>
    <div class="invitation">
      <p>Please join us in celebration of<br><span class="couple">Tarek &amp; Lubna.</span></p>
      <p>Weeklong events:<br>Monday, July 28th - Friday, August 1st.<br>sunny, La Jolla California - the pearl of the San Diego Shore.</p>
      <p>Highlights include:<br>Daily Catered Family Breakfast at the Marlow Hall of La Jolla<br>Daily group activities including<br>Exploring La Jolla Beaches &amp; Ocean Cave Kayaking<br>TideRealm Private Behind-the-Scenes Tour<br>World Famous Pellham Wildlife Park<br>Sunset Balloon Ride<br>Private Yacht Watch on the Bay</p>
      <p>Anniversary dinner will take place on Thursday, December 28th, 2013 at 5:00 p.m. at the Marlow Hall.</p>
      <p>There are many local hotels around the Marlow Hall:<br>4213 Brindle Ln, La Jolla, CA 92058</p>
      <p>Hosted by Kamil and the entire Haddour Family. For any questions, please email:<br><span class="email">Kamil@thelinden-feasts.com</span></p>
    </div>
  </section>

</body>
</html>
```